International Property Consultancy

Detailed Wireframe and info document attached.

Brief Overview:

I need a dynamic and well designed website that is easy to use and understand. It has to be unique and different to generic templates that most websites seem to be these days. PLEASE NO GENERIC TEMPLATES FROM THE INTERNET.

Our business has 10 years experience working on struggling international developments that we then work in-house for to turn around and brings bout success. We stay within a project often for long periods of time until success is achieved. We are unique in our approach and completely different to the standard routes to market for many developments. The site is for developers to see what we have done in regards to previous projects, as such we want to incorporate video into this site with a strong design aesthetic. There will be videos of the past projects we have worked on, which will act as case studies.

I like very simple but punchy websites, that people can navigate and understand very easily. Also a big fan of unique and well thought out design aesthetic.

Initial Site layout thoughts:

1) Homepage:
2) About Us
3) What we've done / Work
This part has the projects we have worked on (France, Portugal, London, Morocco). Each one will have some video content and photo images, but also would be good to have a succinct way to mention what we did and the successes in a clever and punchy way.

4) Contact Us

* This is just a guideline. Would be open to input and creative direction on your own part.

*More details and websites we like can be seen in the brief doc attached.

PLEASE VIEW THE WIREFRAME WORD DOC ATTACHED.

Here there are also some more examples to help:

Here are just a few examples of websites and what I like about them:

- www.velmorit.com (clean, nice geometric design aesthetic, good animation when loading and changing pages well thought out all though also coulee be considered a bit dull and basic after the initial homepage slide)
- https://www.farbridgeloop.net (Clean site, quite clinical, lacks video content and doesn't engage greatly).
- https://quiltmarsh.com (minimal, and like how it mixes the design aesthetic more with video and photo content)

- https://www.theamberotter.com (like the layout of this and how it displays the projects and work section)

- https://drov.com (Good use of video content)

- https://crafthalo.studio (minimal to the point and mixes design with video and animation etc...)

Here is another couple of cool websites that may help give you some direction: https://tidewellgroup.com www.drov.com

Hi there, One of the things I thought would be good on the homepage is to add the logo with a 'digital landscape' before flicking down into a slide with video content of the projects... Just an idea but have posted some pics in the brief. We would get this animated for the site. But if you have better ideas, please do run with them. Thanks,

Target Market(s)

Property developers

Number of Pages Required

4 page

Font styles to use
Other font styles liked:
• Read brief

Requirements
Must have
• Needs to be clean, dynamic and easy to follow on desktop and mobile. We will use it as a kind of portfolio website so will need to embed video of past projects we have worked on.

Read brief in docs.
Nice to have
• Clean
Should not have
• Not be another generic template website.
Not have random property stock photos. (We are not a property agency).

```html
<!DOCTYPE html>
<html lang="en">
<head>
<meta charset="utf-8">
<title>Corvanta — International Property Developments</title>
<link rel="stylesheet" href="https://fonts.googleapis.com/css2?family=Montserrat:wght@400;500;600;800&display=swap">
<style>
  :root {
    --ink: #1f1f22;
    --ink-soft: #6a6a6a;
    --accent: #f26a2b;
    --paper: #ffffff;
    --rule: #d9d9d9;
    --photo-top: #5b6a8e;
    --photo-mid: #8d97a6;
    --photo-low: #3f4a5e;
  }
  * { margin: 0; padding: 0; box-sizing: border-box; }
  html, body {
    width: 1200px; height: 651px; overflow: hidden;
    background: var(--paper);
    font-family: "Montserrat", sans-serif;
    color: var(--ink);
  }
  .page { position: relative; width: 1200px; height: 651px; }

  .hero-media {
    position: absolute; left: 671px; top: 0; width: 529px; height: 585px;
    background:
      radial-gradient(ellipse 55% 60% at 68% 70%, rgba(226,196,200,0.75), rgba(226,196,200,0) 70%),
      linear-gradient(160deg, var(--photo-top) 0%, var(--photo-mid) 45%, var(--photo-low) 100%);
  }

  .brand {
    position: absolute; left: 99px; top: 18px;
    font-size: 33px; font-weight: 500; letter-spacing: 0.5px;
    color: var(--ink);
  }

  .menu-toggle { position: absolute; left: 1075px; top: 30px; width: 28px; height: 20px; }

  .eyebrow {
    position: absolute; left: 134px; top: 190px;
    font-size: 26px; font-weight: 500; letter-spacing: 0.42em;
    color: var(--ink);
  }
  .eyebrow-rule {
    position: absolute; left: 135px; top: 228px; width: 139px; height: 3px;
    background: var(--accent);
  }

  .headline {
    position: absolute; left: 132px; top: 250px; z-index: 2;
    font-size: 57px; font-weight: 800; line-height: 60px; letter-spacing: -0.5px;
    white-space: nowrap;
    background: linear-gradient(90deg, #bdbcba 0px, #2a2a2c 70px, #2a2a2c 180px, #9a9892 320px, #e4e1dc 470px, #3a4a6a 560px, #d8d6d2 700px);
    -webkit-background-clip: text; background-clip: text;
    color: transparent;
  }

  .cta {
    position: absolute; left: 133px; top: 393px; width: 171px; height: 48px;
    background: var(--accent); color: #fff;
    font-size: 14.5px; font-weight: 500;
    display: flex; align-items: center; justify-content: center;
    text-decoration: none;
  }

  .slider-nav { position: absolute; left: 99px; top: 519px; display: flex; gap: 7px; }
  .slider-nav button {
    width: 37px; height: 33px; border: 1px solid var(--ink); background: var(--paper);
    display: flex; align-items: center; justify-content: center;
  }

  .site-footer {
    position: absolute; left: 0; top: 585px; width: 1200px; height: 66px;
    border-top: 1px solid var(--rule);
  }
  .copyright {
    position: absolute; left: 93px; top: 28px;
    font-size: 11.5px; font-weight: 500; letter-spacing: 0.3px; color: var(--ink-soft);
  }
  .social { position: absolute; left: 945px; top: 21px; display: flex; gap: 13px; list-style: none; }
  .social li { width: 27px; height: 27px; border-radius: 50%; background: var(--ink); }
</style>
</head>
<body>
<main class="page">
  <div class="hero-media" role="img" aria-label="Photo of a businesswoman reading a folder in front of a glass dome"></div>

  <header>
    <div class="brand">corvanta.</div>
    <svg class="menu-toggle" viewBox="0 0 28 20" aria-label="Menu">
      <rect x="6" y="1" width="22" height="2.4" fill="#fff"/>
      <rect x="0" y="8.8" width="28" height="2.4" fill="#fff"/>
      <rect x="6" y="16.6" width="22" height="2.4" fill="#fff"/>
    </svg>
  </header>

  <section class="hero-copy">
    <p class="eyebrow">We are Corvanta</p>
    <span class="eyebrow-rule"></span>
    <h1 class="headline">We Fulfill International<br>Property Developments</h1>
    <a class="cta" href="#work">SEE OUR WORK</a>
    <div class="slider-nav">
      <button aria-label="Previous"><svg width="8" height="12" viewBox="0 0 8 12"><path d="M6 1 1.5 6 6 11" fill="none" stroke="#1f1f22" stroke-width="1.8"/></svg></button>
      <button aria-label="Next"><svg width="8" height="12" viewBox="0 0 8 12"><path d="M2 1 6.5 6 2 11" fill="none" stroke="#1f1f22" stroke-width="1.8"/></svg></button>
    </div>
  </section>

  <footer class="site-footer">
    <p class="copyright">COPYRIGHT © 2020 COMPANY ALL RIGHTS RESERVED.</p>
    <ul class="social" aria-label="Social links">
      <li></li><li></li><li></li><li></li>
    </ul>
  </footer>
</main>
</body>
</html>
```